private relaxation massage therapist business card

I want a card that does not give a physical address as I am able to massage at home as well as be mobile. I want on the back somewhere to put appointment details and also my bank acct details for payment being to acct 38 7402 0061948 00
I have a Certificate in Relaxation Massage from KPTA 2014
I would like to use blue colours and maybe have some fluffy clouds somewhere on the business card.

Industry/Entity Type

Massage

Contact Information for Business Card

Fiona Marsh
Relaxation Massage Therapist

telephone 0216 842 197 or 09 4718335
email fionamarsh72@quellbox.com

Requirements
Must have
• bold lettering, lots of white space, On the reverse of the card some lines in a box for me to write appointment times also on reverse my bank acct details for payment on line.

```html
<!DOCTYPE html>
<html lang="en">
<head>
<meta charset="utf-8">
<title>Fiona Marsh — Relaxation Massage Therapist business card</title>
<link rel="stylesheet" href="https://fonts.googleapis.com/css2?family=Lato:wght@300;400&display=swap">
<style>
  :root {
    --backdrop: #646564;
    --card: #ffffff;
    --sky: #8affff;
    --sky-line: #7ef6f6;
    --sky-soft: #dcffff;
    --sky-faint: #f2ffff;
    --ink: #5e5e5e;
    --ink-mid: #7c7c7c;
    --ink-light: #9a9a9a;
  }
  * { margin: 0; padding: 0; box-sizing: border-box; }
  html, body {
    width: 1200px;
    height: 1000px;
    overflow: hidden;
    background: var(--backdrop);
    font-family: "Lato", sans-serif;
  }
  .stage { position: relative; width: 1200px; height: 1000px; }

  .card {
    position: absolute;
    width: 535px;
    height: 325px;
    background: var(--card);
    overflow: hidden;
  }
  .card--front { left: 355px; top: 109px; }
  .card--back { left: 357px; top: 499px; }

  /* Front */
  .accent-bar {
    position: absolute;
    left: 413px;
    top: 0;
    width: 62px;
    height: 188px;
    background: var(--sky);
  }
  .identity {
    position: absolute;
    right: 66px;
    top: 26px;
    text-align: right;
    font-weight: 300;
  }
  .identity__name {
    font-size: 21px;
    letter-spacing: 0.3px;
    color: var(--ink);
    line-height: 22px;
    text-transform: uppercase;
    font-weight: 300;
  }
  .identity__role {
    font-size: 12px;
    color: var(--ink-light);
    line-height: 14px;
    margin-top: 3px;
  }
  .contact {
    list-style: none;
    margin-top: 7px;
    font-size: 11px;
    line-height: 14.5px;
    color: var(--ink-mid);
  }

  .clouds {
    position: absolute;
    border: 2px solid var(--sky-line);
  }
  .clouds--front {
    left: -2px;
    top: 68px;
    width: 457px;
    height: 262px;
    border-radius: 70px 110px 0 0;
    background: linear-gradient(170deg, var(--sky-soft) 0%, var(--sky-faint) 55%, var(--card) 100%);
  }

  /* Back */
  .clouds--back {
    left: 48px;
    top: 46px;
    width: 445px;
    height: 210px;
    border-width: 1px;
    border-radius: 100px;
    background: linear-gradient(180deg, var(--sky-faint) 0%, var(--card) 100%);
  }
  .appointment-lines {
    position: absolute;
    left: 117px;
    top: 110px;
    width: 302px;
  }
  .appointment-lines span {
    display: block;
    height: 2px;
    background: var(--sky);
    margin-bottom: 49px;
  }
  .payment {
    position: absolute;
    left: 194px;
    top: 291px;
    display: flex;
    align-items: center;
    gap: 6px;
    font-size: 13px;
    font-weight: 300;
    color: var(--sky-line);
  }
</style>
</head>
<body>
<main class="stage">
  <section class="card card--front" aria-label="Card front">
    <div class="clouds clouds--front" role="img" aria-label="Outlined fluffy clouds illustration"></div>
    <div class="accent-bar"></div>
    <div class="identity">
      <h1 class="identity__name">Fiona Marsh</h1>
      <p class="identity__role">Relaxation Massage Therapist</p>
      <ul class="contact">
        <li>0216 842 197 |T</li>
        <li>09 4718335 |T</li>
        <li>fionamarsh72@quellbox.com |E</li>
      </ul>
    </div>
  </section>

  <section class="card card--back" aria-label="Card back">
    <div class="clouds clouds--back" role="img" aria-label="Faint outlined clouds illustration"></div>
    <div class="appointment-lines" aria-label="Appointment writing lines">
      <span></span><span></span><span></span>
    </div>
    <p class="payment">
      <svg width="18" height="13" viewBox="0 0 18 13" aria-hidden="true">
        <rect x="0" y="0" width="18" height="13" rx="1.5" fill="var(--sky)"/>
        <rect x="0" y="3" width="18" height="2" fill="#ffffff"/>
        <rect x="2" y="8" width="6" height="1.5" fill="#ffffff"/>
      </svg>
      38 7402 0061948 00
    </p>
  </section>
</main>
</body>
</html>
```